Bramble Hollow Networks - Electrical

We need flyers for electrical services.
Areas of work include new builds, office fitouts, switchboard upgrades, installation of ceiling fans, powerpoint and downlight upgrades, home theatre and AV systems, all exterior and emergency work. Free quotes
We would like to see designs with the colour Red with a young and modern design. Licence No: 63914K must be included and call Leopold on 0438917062.

Colors
ec1f27

```html
<!DOCTYPE html>
<html lang="en">
<head>
<meta charset="utf-8">
<title>Bramble Hollow Networks – Electrical Flyer</title>
<link href="https://fonts.googleapis.com/css2?family=Bebas+Neue&family=Roboto+Condensed:wght@500;700&family=Montserrat:wght@400;700;800&display=swap" rel="stylesheet">
<style>
  :root{
    --red:#ec1f27;
    --black:#0d0d0d;
    --white:#ffffff;
    --paper:#f1f1f1;
    --grey:#a6a6a6;
    --ink:#1d1d1d;
    --yellow:#fff200;
    --silver:#d9d9d9;
  }
  *{margin:0;padding:0;box-sizing:border-box}
  html,body{width:903px;height:1200px;overflow:hidden;background:var(--paper)}
  .flyer{position:relative;width:903px;height:1200px;overflow:hidden;background:var(--paper)}
  .backdrop{position:absolute;inset:0}
  .headline{position:absolute;left:46px;top:36px;font-family:"Bebas Neue",sans-serif;font-weight:400;color:var(--white);line-height:.9}
  .headline .small{display:block;font-size:74px}
  .headline .big{display:block;font-size:130px;color:var(--red);margin:4px 0 4px}
  .badge{position:absolute;left:622px;top:66px;width:248px;height:248px;border-radius:50%;
    background:radial-gradient(circle at 35% 30%,#ffffff,var(--silver) 55%,#9a9a9a);box-shadow:0 4px 12px rgba(0,0,0,.4)}
  .badge-inner{position:absolute;inset:14px;border-radius:50%;background:var(--yellow);
    display:flex;flex-direction:column;align-items:center;justify-content:center;font-family:"Bebas Neue",sans-serif;line-height:.9}
  .badge-pct{font-size:88px;color:var(--red)}
  .badge-text{font-size:40px;color:var(--ink);text-align:center}
  .areas{position:absolute;left:462px;top:656px}
  .areas-title{font-family:"Roboto Condensed",sans-serif;font-weight:700;font-size:40px;color:var(--grey);margin-left:31px;letter-spacing:.5px}
  .areas-list{list-style:none;margin-top:8px}
  .areas-list li{display:flex;align-items:center;height:48px;font-family:"Roboto Condensed",sans-serif;font-weight:500;font-size:27px;color:var(--ink)}
  .areas-list svg{width:24px;height:24px;margin-right:11px;fill:var(--red)}
  .quote-bar{position:absolute;left:269px;top:1000px;width:634px;height:53px;background:var(--red);
    font-family:"Montserrat",sans-serif;font-size:26px;color:var(--white);display:flex;align-items:center;justify-content:flex-end;padding-right:25px}
  .quote-bar strong{color:var(--yellow);font-weight:700;margin-left:8px}
  .phone{position:absolute;right:28px;top:1062px;font-family:"Montserrat",sans-serif;font-weight:800;font-size:80px;color:var(--ink);letter-spacing:-2px;line-height:1.1}
  .licence{position:absolute;right:30px;top:1152px;font-family:"Montserrat",sans-serif;font-weight:700;font-size:20px;letter-spacing:6px;color:var(--ink)}
</style>
</head>
<body>
<main class="flyer">
  <svg class="backdrop" width="903" height="1200" viewBox="0 0 903 1200">
    <defs>
      <linearGradient id="panelTones" x1="0" y1="0" x2="1" y2="1">
        <stop offset="0" stop-color="#e6e6e6"/><stop offset=".5" stop-color="#c9cfd4"/><stop offset="1" stop-color="#4d7fa8"/>
      </linearGradient>
      <linearGradient id="workerTones" x1="0" y1="0" x2="0" y2="1">
        <stop offset="0" stop-color="#3a3f5c"/><stop offset="1" stop-color="#1f2545"/>
      </linearGradient>
    </defs>
    <polygon class="dark-field" points="0,0 903,0 903,110 0,870" fill="var(--black)"/>
    <polygon class="bolt" points="903,108 903,168 520,400 660,548 0,875 0,805 430,560 300,470" fill="var(--red)"/>
    <polygon class="panel-photo" role="img" aria-label="Photo of a hand testing a switchboard with coloured wiring"
      points="903,168 903,645 645,548 520,400" fill="url(#panelTones)"/>
    <rect class="worker-photo" role="img" aria-label="Photo of a smiling young electrician with hard hat, cable coil and tool belt"
      x="0" y="340" width="360" height="860" fill="url(#workerTones)"/>
  </svg>

  <h1 class="headline">
    <span class="small">Need an</span>
    <span class="big">Electrician</span>
    <span class="small">In your area</span>
  </h1>

  <div class="badge">
    <div class="badge-inner">
      <span class="badge-pct">100%</span>
      <span class="badge-text">Satisfaction<br>Guaranteed</span>
    </div>
  </div>

  <section class="areas">
    <h2 class="areas-title">AREAS OF WORK</h2>
    <ul class="areas-list">
      <li><svg viewBox="0 0 24 24"><path d="M12 2 1 12h3v10h6v-6h4v6h6V12h3z"/></svg>New Builds, Office Fitouts</li>
      <li><svg viewBox="0 0 24 24"><path d="M3 3h18v18H3zM7 7v3h3V7zm7 0v3h3V7zM7 14v3h3v-3zm7 0v3h3v-3z" fill-rule="evenodd"/></svg>Switchboard Upgrades</li>
      <li><svg viewBox="0 0 24 24"><circle cx="12" cy="12" r="3"/><path d="M10 10 6 2h8zM14 13l8 4-5 6zM10 13l-8 4 5 6z"/></svg>Installation of Ceiling Fans</li>
      <li><svg viewBox="0 0 24 24"><path d="M12 4a6 6 0 0 0-4 10.5V18h8v-3.5A6 6 0 0 0 12 4zM9 20h6v2H9zM11 0h2v2h-2zM1 9h2v2H1zm20 0h2v2h-2z"/></svg>PowerPoint &amp; Downlight Upgrades</li>
      <li><svg viewBox="0 0 24 24"><path d="M0 4h5v16H0zM19 4h5v16h-5zM6 5h12v11H6zM9 18h6v2H9z"/></svg>Home Theatre &amp; AV Systems</li>
      <li><svg viewBox="0 0 24 24"><path d="M12 2a10 10 0 1 0 0 20 10 10 0 0 0 0-20zm0 3a7 7 0 1 1-7 7h4a3 3 0 1 0 3-3zm-8 3h5v2H4zm0 4h5v2H4z" fill-rule="evenodd"/></svg>All Exterior &amp; Emergency work</li>
    </ul>
  </section>

  <div class="quote-bar">Call Leopold For <strong>Get A Free Quote</strong></div>
  <div class="phone">0438 917 062</div>
  <div class="licence">LICENCE NO: 63914K</div>
</main>
</body>
</html>
```